Orbeo app design for cryptocurrency trading investment fund Vornexa

Vornexa is an investment fund that help investors with investing in cryptocurrencies such as Zentrix and Pallidor. We use our own trading platform to buy and sell crypto currencies on behalf of the investors. As an extra service we want to develop an Orbeo app for our investors. After logging in the Orbeo app they can get a real-time insight in the value of their portfolio. We have created wireframes of these pages in attached zip file. This zip file also contains the logo of Vornexa.

We need you to design a clean professional and fresh app design based on the wireframes. The app design should contain the corporate identity of Vornexa and thus the following color codes and font type must be used:

Color 1: 489e95
Color 2: 474646
Font type: Open Sans

login.png
The investor first has to login the app

home.png
The first page the investor sees after logging in.

account.png
In the account section the investor can change his login access details to the app

account_b.png
On this page he can change his password.

Coin page (added as separate file)
This is the page that shows up when you click on one of the coins.

Target Market(s)

Investors who invest the minimum amount of € 100.000

Industry/Entity Type

Tech

Requirements
Must have
• Professional modern design
Should not have
• cheap colourful creative look and feel.

```html
<!DOCTYPE html>
<html lang="en">
<head>
<meta charset="utf-8">
<title>Vornexa – Orbeo app screens</title>
<link rel="stylesheet" href="https://fonts.googleapis.com/css2?family=Open+Sans:wght@300;400;600&display=swap">
<style>
:root{
  --brand:#489e95;
  --ink:#474646;
  --stage:#161616;
  --label:#8a8a8a;
  --muted:#9a9a9a;
  --rule:#d6d6d6;
  --panel:#f2f2f2;
  --up:#3aa43a;
  --down:#c8363b;
  --chart-blue:#2aa8ee;
  --chart-red:#ee1558;
  --white:#ffffff;
}
*{box-sizing:border-box;margin:0;padding:0}
html,body{width:1200px;height:1200px;overflow:hidden;background:var(--stage)}
body{font-family:"Open Sans",Arial,sans-serif;color:var(--ink)}
.canvas{position:relative;width:1200px;height:1200px}
.abs{position:absolute;white-space:nowrap}

.brand-mark{position:absolute;left:862px;top:44px;display:flex;align-items:center;gap:14px}
.brand-mark .dot{width:50px;height:50px;border-radius:50%;background:var(--brand)}
.brand-mark .name{font-size:62px;font-weight:400;color:var(--white);line-height:1}

.section-title{position:absolute;font-size:40px;font-weight:400;color:var(--label);line-height:1}

.screen{position:absolute;width:317px;height:563px;background:var(--white);overflow:hidden}
.screen--splash{left:63px;top:209px}
.screen--login{left:423px;top:384px;height:562px}
.screen--home{left:783px;top:553px}

.status-bar{position:absolute;left:0;top:0;width:100%;height:15px;font-size:8px;color:#6f6f6f;display:flex;align-items:center;padding:0 6px}
.status-bar .carrier{display:flex;align-items:center;gap:4px}
.status-bar .signal{letter-spacing:-1px;font-size:7px}
.status-bar .time{position:absolute;left:50%;transform:translateX(-50%)}
.status-bar .right{position:absolute;right:6px;display:flex;align-items:center;gap:4px}
.battery{width:20px;height:7px;border:1px solid currentColor;padding:1px}
.battery i{display:block;width:100%;height:100%;background:currentColor}
.status-bar--light{color:var(--white)}

.wordmark{position:absolute;left:0;width:100%;display:flex;justify-content:center;align-items:center;gap:6px}
.wordmark .dot{border-radius:50%;background:var(--brand)}
.wordmark .name{color:var(--ink);font-weight:400;line-height:1}

/* login */
.welcome{top:122px;width:100%;text-align:center;font-size:13px}
.intro{top:145px;left:20px;width:277px;text-align:center;font-size:9.6px;line-height:11.7px;white-space:normal}
.field-label{font-size:10px;left:22px}
.placeholder{font-size:10px;color:var(--muted);left:22px}
.rule{position:absolute;left:14px;width:289px;height:1px;background:var(--rule)}
.forgot{right:26px;font-size:10px;color:var(--brand)}
.checkbox{position:absolute;left:23px;top:323px;width:14px;height:14px;border:1.2px solid #777;border-radius:2px}
.btn-login{position:absolute;left:82px;top:366px;width:152px;height:39px;background:var(--brand);border-radius:3px;color:var(--white);font-size:12.5px;display:flex;align-items:center;justify-content:center;box-shadow:0 1px 2px rgba(0,0,0,.25)}
.signup{top:440px;width:100%;text-align:center;font-size:10px}
.signup b{color:var(--brand);font-weight:400;font-size:11.5px}
.progress{position:absolute;left:0;bottom:0;width:100%;height:3px;background:#3a3a3a}
.progress i{display:block;width:50%;height:100%;background:var(--brand)}

/* home */
.app-header{position:absolute;left:0;top:0;width:100%;height:50px;background:var(--brand)}
.app-header .name{color:var(--white)}
.summary{position:absolute;left:0;top:50px;width:100%;height:126px;background:var(--panel)}
.balance-label{top:17px;left:96px;font-size:10px}
.up{color:var(--up)}
.down{color:var(--down)}
.balance{top:33px;width:100%;text-align:center;font-size:27px;color:var(--brand);font-weight:400}
.small-label{font-size:10px}
.value{font-size:13px}

.coin-table{position:absolute;left:10px;top:185px;width:297px;border-collapse:collapse;font-size:10px}
.coin-table th{font-weight:600;text-align:center;height:21px;font-size:10.2px}
.coin-table td{text-align:center;height:22px}
.coin-table th:first-child,.coin-table td:first-child{text-align:left;width:50px}
.divider{position:absolute;left:0;width:100%;height:1px;background:#e2e2e2}

.chart-title{top:313px;left:10px;font-size:10.5px}
.periods{position:absolute;top:328px;left:0;width:100%;font-size:6.5px;color:var(--muted)}
.periods span{position:absolute;transform:translateX(-50%)}
.periods .active{background:#8a8a8a;color:var(--white);padding:1px 7px;border-radius:6px;top:-1px}
.axis{font-size:7px;color:#777;left:14px}
.months{font-size:7px;color:#777}
.tabbar{position:absolute;left:0;top:530px;width:100%;height:33px}
.tab{position:absolute;transform:translateX(-50%);text-align:center;font-size:6px;color:#aaa}
.tab svg{display:block;margin:0 auto 2px}
.tab--active{color:var(--brand)}
</style>
</head>
<body>
<div class="canvas">

  <div class="brand-mark"><span class="dot"></span><span class="name">Vornexa</span></div>

  <div class="section-title" style="left:98px;top:143px">Splash</div>
  <div class="section-title" style="left:458px;top:315px">Login</div>
  <div class="section-title" style="left:812px;top:483px">Home</div>

  <!-- Splash -->
  <section class="screen screen--splash" aria-label="Splash screen">
    <div class="status-bar">
      <span class="carrier"><span class="signal">●●●●●</span>Nordwave</span>
      <span class="time">9:41 AM</span>
      <span class="right">◉ ➚ ⏰ 100% <span class="battery"><i></i></span></span>
    </div>
    <div class="wordmark" style="top:264px">
      <span class="dot" style="width:28px;height:28px"></span>
      <span class="name" style="font-size:36px">Vornexa</span>
    </div>
  </section>

  <!-- Login -->
  <section class="screen screen--login" aria-label="Login screen">
    <div class="status-bar">
      <span class="carrier"><span class="signal">●●●●●</span>Nordwave</span>
      <span class="time">9:41 AM</span>
      <span class="right">◉ ➚ ⏰ 100% <span class="battery"><i></i></span></span>
    </div>
    <div class="wordmark" style="top:72px">
      <span class="dot" style="width:22px;height:22px"></span>
      <span class="name" style="font-size:28px">Vornexa</span>
    </div>
    <div class="abs welcome">Welcome to the Vornexa app</div>
    <p class="abs intro">Lorem Ipsum is simply dummy text of the printing and typesetting industry. Lorem Ipsum has been the industry's standard dummy text ever since the 1500s,</p>

    <div class="abs field-label" style="top:207px">Email</div>
    <div class="abs placeholder" style="top:228px">Your email</div>
    <div class="rule" style="top:251px"></div>

    <div class="abs field-label" style="top:262px">Password</div>
    <div class="abs" style="left:22px;top:285px;font-size:8px;letter-spacing:1px">•••••••••</div>
    <div class="abs forgot" style="top:283px">Forgot?</div>
    <div class="rule" style="top:305px"></div>

    <span class="checkbox"></span>
    <div class="abs" style="left:48px;top:323px;font-size:10px">Stay connected</div>

    <div class="btn-login">LOGIN</div>
    <div class="abs signup">Create own account? <b>Signup</b></div>
    <div class="progress"><i></i></div>
  </section>

  <!-- Home -->
  <section class="screen screen--home" aria-label="Home screen">
    <header class="app-header">
      <div class="status-bar status-bar--light">
        <span class="carrier"><span class="signal">●●●●●</span>Nordwave</span>
        <span class="time">9:41 AM</span>
        <span class="right">◉ ➚ ⏰ 100% <span class="battery"><i></i></span></span>
      </div>
      <div class="wordmark" style="top:25px">
        <span class="dot" style="width:13px;height:13px;background:var(--white)"></span>
        <span class="name" style="font-size:16px">Vornexa</span>
      </div>
    </header>

    <div class="summary">
      <div class="abs balance-label">Current Balance <span class="up" style="margin-left:18px">110% ↑</span></div>
      <div class="abs balance">€&nbsp; 110.000,00</div>
      <div class="abs small-label" style="left:27px;top:76px">Invested Amount</div>
      <div class="abs value" style="left:27px;top:93px">€&nbsp; 100.000,00</div>
      <div class="abs small-label" style="left:199px;top:76px">Profit/loss <span class="up" style="margin-left:10px">10 %</span></div>
      <div class="abs value" style="left:199px;top:93px">€&nbsp; 10.000,00</div>
    </div>

    <table class="coin-table">
      <tr><th>COIN</th><th>PLD/EUR</th><th>KVR</th><th>LMO</th><th>ZTX</th><th>QRA</th></tr>
      <tr><td>Change</td><td class="up">+9.4%</td><td class="down">-15.11%</td><td class="up">+4.4%</td><td class="down">-1.6%</td><td class="up">+9.24%</td></tr>
      <tr><td>Price (€)</td><td>295,22</td><td>45,89</td><td>235,56</td><td>2.400,05</td><td>2,03</td></tr>
      <tr><td>Holdings</td><td>2.552</td><td>132.009</td><td>38.236</td><td>59.60</td><td>4.952</td></tr>
      <tr><td>H (€)</td><td>755.87K</td><td>556.72K</td><td>255.40K</td><td>143.36K</td><td>10.044</td></tr>
    </table>
    <div class="divider" style="top:302px"></div>

    <div class="abs chart-title">Portfolio Chart</div>
    <div class="periods">
      <span style="left:115px">1D</span><span style="left:144px">7D</span><span style="left:173px">1M</span>
      <span class="active" style="left:203px">3M</span><span style="left:232px">6M</span><span style="left:261px">1Y</span><span style="left:291px">ALL</span>
    </div>

    <div class="abs axis" style="top:353px">300</div>
    <div class="abs axis" style="top:377px">250</div>
    <div class="abs axis" style="top:402px">200</div>
    <div class="abs axis" style="top:428px">150</div>
    <div class="abs axis" style="top:453px">100</div>
    <div class="abs axis" style="top:477px;left:18px">50</div>

    <svg class="abs" style="left:0;top:0" width="317" height="563" viewBox="0 0 317 563" aria-label="Portfolio line chart">
      <line x1="36" y1="498" x2="290" y2="498" stroke="#ececec"/>
      <polyline fill="none" stroke="var(--chart-blue)" stroke-width="1.6" points="41,457 78,423 93,437 125,410 146,377 174,399 229,383 275,405"/>
      <polyline fill="none" stroke="var(--chart-red)" stroke-width="1.6" points="41,491 78,468 97,484 139,450 172,485 184,435 201,454 245,430 274,458"/>
      <circle cx="146" cy="377" r="3" fill="var(--chart-blue)"/>
      <rect x="123" y="356" width="46" height="14" rx="3" fill="var(--chart-blue)"/>
      <path d="M143 370 L146 373 L149 370 Z" fill="var(--chart-blue)"/>
      <text x="146" y="366" font-size="7" fill="#fff" text-anchor="middle" font-family="Open Sans, sans-serif">265,098</text>
    </svg>

    <div class="abs months" style="left:75px;top:505px">April</div>
    <div class="abs months" style="left:150px;top:505px">May</div>
    <div class="abs months" style="left:222px;top:505px">June</div>

    <nav class="tabbar">
      <div class="tab tab--active" style="left:54px">
        <svg width="16" height="18" viewBox="0 0 16 18"><path d="M5 16V3M2 6l3-3 3 3M11 2v13M8 12l3 3 3-3" fill="none" stroke="var(--brand)" stroke-width="1.6"/></svg>Dashboard
      </div>
      <div class="tab" style="left:158px">
        <svg width="18" height="18" viewBox="0 0 18 18"><path d="M2 1v16h16" fill="none" stroke="#aaa"/><polyline points="4,13 8,8 11,11 16,4" fill="none" stroke="#aaa" stroke-width="1.2"/></svg>Portfolio
      </div>
      <div class="tab" style="left:264px">
        <svg width="16" height="18" viewBox="0 0 16 18"><circle cx="8" cy="5" r="4" fill="#bbb"/><path d="M1 17c0-5 3-7 7-7s7 2 7 7z" fill="#bbb"/></svg>Account
      </div>
    </nav>
  </section>

</div>
</body>
</html>
```